Business Card Design for BrightwaveOutreach.com

--I need a business card design for my company BrightwaveOutreach.com

I have attached my logo...I want the brightwave outreach logo on the front of the business card, and then I want The Brightwave Chief on the back of it with my information.

I would like to see a light colored background as well as a dark colored background

FRONT:
BRIGHTWAVE OUTREACH LOGO
482 N. Elmwood
5th Floor
Fairhaven OR 97215
www.BrightwaveOutreach.com

Advanced Website & App Development
Websites, Apps, Online Voucher Systems

Leading Edge Marketing Services
SMS, VB, SMM, SEM,

BACK:
BRIGHTWAVE CHIEF LOGO
Dorian Pelley
The Brightwave Chief
Call Or Text: 619-555-0148
Dorian@BrightwaveChief.com
www.BrightwaveChief.com

Target Market(s)

small business owners

Industry/Entity Type

Business Consultant

Contact Information for Business Card

FRONT:
BRIGHTWAVE OUTREACH LOGO
482 N. Elmwood
5th Floor
Fairhaven OR 97215
www.BrightwaveOutreach.com

SMS, VB, SMM, SEM,

BACK:
BRIGHTWAVE CHIEF LOGO
Dorian Pelley
The Brightwave Chief
Dorian@BrightwaveChief.com
www.BrightwaveChief.com

Requirements
Must have
• add this quote on it somewhere, anywhere,preferrably on back
• "The Fastest Way To Success Is To Take Action”
• — Dorian Pelley, Brightwave Chief
Nice to have
• open
Should not have
• red

```html
<!DOCTYPE html>
<html lang="en">
<head>
<meta charset="utf-8">
<title>Brightwave Outreach Business Cards</title>
<link rel="stylesheet" href="https://fonts.googleapis.com/css2?family=Archivo+Black&family=Exo+2:wght@500;600&family=Montserrat:wght@400;500&display=swap">
<style>
  :root {
    --bg: #3a3a3a;
    --card: #050505;
    --blue: #1a7fc1;
    --white: #ffffff;
    --rule: #d8d8d8;
  }
  * { box-sizing: border-box; margin: 0; padding: 0; }
  html, body { width: 1200px; height: 900px; overflow: hidden; }
  body {
    background: var(--bg);
    position: relative;
    font-family: "Montserrat", Arial, sans-serif;
    color: var(--white);
  }
  .card {
    position: absolute;
    width: 560px;
    height: 320px;
    background: var(--card);
    border-radius: 22px;
    overflow: hidden;
    box-shadow: 0 18px 40px rgba(0,0,0,.45);
  }
  .card-front { left: 60px; top: 110px; }
  .card-back { left: 580px; top: 470px; }

  /* front */
  .front-inner {
    position: absolute; left: 0; right: 0; top: 30px;
    text-align: center;
  }
  .brand-name {
    font-family: "Montserrat", Arial, sans-serif;
    font-weight: 500;
    color: var(--blue);
    letter-spacing: 3px;
    line-height: 1.05;
  }
  .brand-name--front { font-size: 38px; }
  .brand-subline {
    display: flex; align-items: center; justify-content: center; gap: 12px;
    margin-top: 2px;
  }
  .brand-subline::before, .brand-subline::after {
    content: ""; width: 90px; height: 1px; background: var(--rule);
  }
  .brand-subline span {
    font-size: 18px; letter-spacing: 7px; color: var(--white);
  }
  .address {
    margin-top: 10px;
    font-size: 13.5px;
    line-height: 1.35;
  }
  .address .accent { color: var(--blue); }
  .services {
    margin-top: 14px;
    font-family: "Archivo Black", Arial, sans-serif;
    font-size: 11px;
    line-height: 1.45;
    letter-spacing: .3px;
  }
  .services .cap { font-size: 16px; }
  .marketing {
    margin-top: 10px;
    font-family: "Exo 2", Arial, sans-serif;
    font-weight: 500;
    color: var(--blue);
    font-size: 13px;
    letter-spacing: 2.6px;
    line-height: 1.45;
  }

  /* back */
  .back-logo {
    position: absolute; left: 38px; top: 112px;
    width: 250px; text-align: right;
  }
  .brand-name--back { font-size: 27px; }
  .brand-name--back .line2 { display: block; font-size: 15px; letter-spacing: 6px; }
  .divider {
    position: absolute; left: 306px; top: 66px;
    width: 1px; height: 120px; background: var(--rule);
  }
  .contact { position: absolute; left: 326px; top: 60px; }
  .person-name {
    font-family: "Exo 2", Arial, sans-serif;
    font-weight: 600; font-size: 22px; color: var(--blue);
    letter-spacing: 1px;
  }
  .person-title { font-size: 13px; margin-bottom: 6px; }
  .contact-list { list-style: none; font-size: 13px; line-height: 1.5; }
  .contact-list li { display: flex; align-items: center; gap: 7px; }
  .contact-list svg { width: 10px; height: 10px; fill: var(--blue); flex: none; }
  .contact-list .accent { color: var(--blue); }
  .quote-band {
    position: absolute; left: 0; right: 0; bottom: 30px; height: 26px;
    background: var(--white);
  }
  .quote-bar {
    position: absolute; left: 90px; right: 70px; top: -3px; bottom: -3px;
    background: var(--blue);
    border: 2px solid var(--white);
    display: flex; align-items: center; justify-content: center;
    font-family: "Exo 2", Arial, sans-serif; font-weight: 600;
    font-size: 12.5px; letter-spacing: 1.8px; color: var(--white);
    text-transform: uppercase;
  }
</style>
</head>
<body>

<section class="card card-front" aria-label="Front of business card">
  <div class="front-inner">
    <div class="brand-name brand-name--front">BRIGHTWAVE</div>
    <div class="brand-subline"><span>OUTREACH</span></div>
    <p class="address">482 N. Elmwood , 5th Floor<br>Fairhaven OR 97215<br>www.<span class="accent">BrightwaveOutreach</span>.com</p>
    <p class="services">
      <span class="cap">A</span>dvanced <span class="cap">W</span>ebsite &amp; <span class="cap">A</span>pp <span class="cap">D</span>evelopment<br>
      <span class="cap">W</span>ebsites, <span class="cap">A</span>pps, <span class="cap">O</span>nline <span class="cap">V</span>oucher <span class="cap">S</span>ystems
    </p>
    <p class="marketing">LEADING EDGE MARKETING SERVICES<br>SMS, VB, SMM, SEM,</p>
  </div>
</section>

<section class="card card-back" aria-label="Back of business card">
  <div class="back-logo">
    <div class="brand-name brand-name--back">BRIGHTWAVE<span class="line2">CHIEF</span></div>
  </div>
  <div class="divider"></div>
  <div class="contact">
    <div class="person-name">DORIAN PELLEY</div>
    <div class="person-title">CEO</div>
    <ul class="contact-list">
      <li><svg viewBox="0 0 10 10"><path d="M2 0.5 L3.6 0.5 L4.2 2.8 L3 3.6 Q4 6 6.4 7 L7.2 5.8 L9.5 6.4 L9.5 8 Q9.5 9.5 8 9.5 Q0.5 9 0.5 2 Q0.5 0.5 2 0.5Z"/></svg><span>619-555-0148</span></li>
      <li><svg viewBox="0 0 10 10"><path d="M0.5 2 H9.5 V8.5 H0.5Z M1.2 2.6 L5 5.6 L8.8 2.6" fill="none" stroke="#1a7fc1" stroke-width="1.1"/></svg><span>Dorian@BrightwaveChief.com</span></li>
      <li><svg viewBox="0 0 10 10"><circle cx="5" cy="5" r="4.3" fill="none" stroke="#1a7fc1" stroke-width="1.1"/><path d="M0.7 5 H9.3 M5 0.7 Q2.4 5 5 9.3 Q7.6 5 5 0.7" fill="none" stroke="#1a7fc1" stroke-width="0.9"/></svg><span>www.<span class="accent">BrightwaveChief</span>.com</span></li>
    </ul>
  </div>
  <div class="quote-band">
    <div class="quote-bar">The fastest way to success is to take action</div>
  </div>
</section>

</body>
</html>
```